The Drawer Sage needs a business card

The drawer sage is a lead generation service serving the Custom Closet industry.

Here is the basic card information:

The Drawer Sage
Gregory Tessman
Owner/CEO
Maple Falls, NC
704-555-0183 Cell
Email: gtessman@TheDrawerSage.example

Additional information for the card:

"Flat rate, high quality leads made only for the custom cabinet and storage trade"

Bullet points for the back:

- Low fixed cost
- Easy to budget
- Guaranteed qualified Leeds
- Exclusivity per city

Logo attached, head shot attached. Photos of closet systems attached

```html
<!DOCTYPE html>
<html lang="en">
<head>
<meta charset="utf-8">
<title>The Drawer Sage — Business Card</title>
<link rel="stylesheet" href="https://fonts.googleapis.com/css2?family=Libre+Baskerville:ital,wght@0,400;0,700;1,400&family=Open+Sans:wght@400;600&display=swap">
<style>
  :root {
    --bg-dark: #1f2022;
    --bg-mid: #3a3b3e;
    --card-white: #ffffff;
    --brand-copper: #a0612a;
    --ink-gray: #4b4b4d;
    --band-gray: #4a4a4c;
    --band-text: #f2f2f2;
    --soft-gray: #7a7a7c;
  }
  * { box-sizing: border-box; margin: 0; padding: 0; }
  html, body { width: 1200px; height: 952px; overflow: hidden; }
  body {
    background: radial-gradient(ellipse at 55% 40%, var(--bg-mid), var(--bg-dark) 75%);
    font-family: "Open Sans", sans-serif;
    position: relative;
  }
  .card {
    position: absolute;
    width: 500px;
    height: 286px;
    background: var(--card-white);
    border-radius: 18px;
    overflow: hidden;
    box-shadow: 0 18px 40px rgba(0,0,0,0.45);
  }
  .card-front { left: 60px; top: 333px; }
  .card-back { left: 640px; top: 333px; }

  /* Front */
  .brand-lockup {
    position: absolute; left: 34px; top: 34px;
    display: flex; align-items: center; gap: 10px;
  }
  .brand-mark {
    width: 12px; height: 12px;
    background: var(--brand-copper);
  }
  .brand-name {
    font-family: "Open Sans", sans-serif;
    font-weight: 600;
    font-size: 22px;
    color: var(--brand-copper);
  }
  .holder { position: absolute; left: 34px; top: 100px; }
  .holder-name {
    font-family: "Libre Baskerville", serif;
    font-weight: 700;
    font-size: 19px;
    letter-spacing: 1px;
    color: var(--brand-copper);
    text-transform: uppercase;
  }
  .holder-title {
    margin-top: 6px;
    font-size: 13px;
    color: var(--soft-gray);
  }
  .contact-list {
    position: absolute; right: 30px; bottom: 30px;
    list-style: none;
    display: flex; flex-direction: column; gap: 9px;
    align-items: flex-end;
  }
  .contact-item {
    display: flex; align-items: center; gap: 10px;
    font-size: 14px; color: var(--ink-gray);
  }
  .contact-icon {
    width: 22px; height: 22px; border-radius: 4px;
    background: var(--brand-copper);
    display: flex; align-items: center; justify-content: center;
  }

  /* Back */
  .tagline {
    position: absolute; left: 40px; right: 40px; top: 58px;
    text-align: center;
    font-family: "Libre Baskerville", serif;
    font-style: italic;
    font-size: 17px;
    line-height: 1.5;
    color: var(--brand-copper);
  }
  .benefit-band {
    position: absolute; left: 0; right: 0; bottom: 0; height: 104px;
    background: var(--band-gray);
    border-top: 4px solid var(--card-white);
    box-shadow: 0 -5px 0 -3px var(--brand-copper);
    padding: 26px 34px 0;
    display: grid; grid-template-columns: 1fr 1.3fr; row-gap: 10px;
  }
  .benefit {
    font-family: "Libre Baskerville", serif;
    font-size: 13px;
    letter-spacing: 1.2px;
    color: var(--band-text);
  }
  .benefit::before { content: "• "; }
</style>
</head>
<body>

<section class="card card-front" aria-label="Business card front">
  <div class="brand-lockup">
    <span class="brand-mark"></span>
    <span class="brand-name">The Drawer Sage</span>
  </div>
  <div class="holder">
    <p class="holder-name">Gregory Tessman</p>
    <p class="holder-title">Owner/CEO</p>
  </div>
  <ul class="contact-list">
    <li class="contact-item">Maple Falls, NC
      <span class="contact-icon">
        <svg width="14" height="14" viewBox="0 0 24 24"><path d="M12 2a7 7 0 0 0-7 7c0 5 7 13 7 13s7-8 7-13a7 7 0 0 0-7-7zm0 9.5A2.5 2.5 0 1 1 12 6.5a2.5 2.5 0 0 1 0 5z" fill="#fff"/></svg>
      </span>
    </li>
    <li class="contact-item">704-555-0183
      <span class="contact-icon">
        <svg width="14" height="14" viewBox="0 0 24 24"><path d="M6.6 10.8a15 15 0 0 0 6.6 6.6l2.2-2.2a1 1 0 0 1 1-.25 11.4 11.4 0 0 0 3.6.6 1 1 0 0 1 1 1V20a1 1 0 0 1-1 1A17 17 0 0 1 3 4a1 1 0 0 1 1-1h3.5a1 1 0 0 1 1 1c0 1.25.2 2.45.6 3.6a1 1 0 0 1-.25 1z" fill="#fff"/></svg>
      </span>
    </li>
    <li class="contact-item">gtessman@TheDrawerSage.example
      <span class="contact-icon">
        <svg width="14" height="14" viewBox="0 0 24 24"><rect x="3" y="5" width="18" height="14" rx="1" fill="none" stroke="#fff" stroke-width="2"/><path d="M3 6l9 7 9-7" fill="none" stroke="#fff" stroke-width="2"/></svg>
      </span>
    </li>
  </ul>
</section>

<section class="card card-back" aria-label="Business card back">
  <p class="tagline">"Flat rate, high quality leads made only for the custom cabinet and storage trade"</p>
  <div class="benefit-band">
    <span class="benefit">Low Fixed Cost</span>
    <span class="benefit">Guaranteed Qualified Leeds</span>
    <span class="benefit">Easy To Budget</span>
    <span class="benefit">Exclusivity Per City</span>
  </div>
</section>

</body>
</html>
```